Web Design for One for One Organic Soap Company

We need a website design for the company Tidewell Botanics based on the package design per attached.

The design should communicate high end, luxury organic. The site will provide facts about how the spread of disease causes deaths and can be prevented with hand washing. The site will also have a page about why we are passionate about organics and how that relates to our skin including skin facts.
Also, the site should have an e-commerce product page and shopping cart.

Target Market(s)

Educated, health conscious and socially conscious consumers who shop luxury. Target vendors include Larkmont Grocers and Velbrook..

Industry/Entity Type

E-Commerce

Font styles to use
Other font styles liked:
• See attached

Requirements
Must have
• Use of Ying Yang leaf Logo provided.
Based on design provided.

```html
<!DOCTYPE html>
<html lang="en">
<head>
<meta charset="utf-8">
<title>Tidewell Botanics — Organic Soap</title>
<link href="https://fonts.googleapis.com/css2?family=PT+Sans:ital,wght@0,400;0,700;1,400&display=swap" rel="stylesheet">
<style>
  :root {
    --page: #f5f5f5;
    --sand: #ccb291;
    --earth: #3a2a17;
    --brick: #a0391e;
    --title-red: #a8321e;
    --heading-tan: #b8966a;
    --ink: #3b2d1f;
    --muted: #9a9a9a;
    --panel: #f4f4f4;
    --white: #ffffff;
    --icon: #2d2a27;
    --rule: #b09774;
  }
  * { margin: 0; padding: 0; box-sizing: border-box; }
  html, body { width: 1200px; height: 1000px; overflow: hidden; }
  body {
    position: relative;
    background: var(--page);
    font-family: "PT Sans", sans-serif;
    color: var(--ink);
  }
  .sand-band { position: absolute; left: 0; top: 333px; width: 1200px; height: 607px; background: var(--sand); }
  .site-footer {
    position: absolute; left: 0; top: 940px; width: 1200px; height: 60px;
    background: var(--earth); color: #a89a86; font-size: 7px; text-align: center;
    padding-top: 29px; line-height: 11px;
  }
  .brand { position: absolute; left: 291px; top: 62px; display: flex; align-items: flex-start; gap: 6px; }
  .brand-mark { width: 24px; height: 38px; background: var(--brick); }
  .brand-text { display: flex; flex-direction: column; }
  .brand-name { font-size: 14px; line-height: 16px; color: var(--earth); margin-top: 0; }
  .brand-tagline { font-size: 12px; line-height: 18px; color: var(--earth); letter-spacing: 1px; }
  .main-nav { position: absolute; top: 75px; left: 458px; height: 25px; }
  .main-nav a {
    position: absolute; top: 0; height: 25px; line-height: 25px;
    font-size: 8px; text-transform: uppercase; text-decoration: none;
    color: var(--ink); white-space: nowrap; transform: translateX(-50%);
  }
  .main-nav a.is-active { background: var(--white); color: var(--title-red); width: 57px; text-align: center; transform: none; left: 0; }
  .hero {
    position: absolute; left: 291px; top: 135px; width: 657px; height: 285px;
    background: linear-gradient(180deg, #faf8f0 0%, #f2efdf 100%);
  }
  .section-title { font-weight: 400; font-size: 14px; line-height: 16px; text-transform: uppercase; }
  .latest { position: absolute; left: 291px; top: 450px; width: 150px; }
  .latest .section-title { color: var(--white); }
  .update { padding: 27px 0 10px; border-bottom: 1px solid var(--rule); }
  .update + .update { padding-top: 11px; }
  .update-date { font-size: 6.5px; font-weight: 700; line-height: 10px; margin-bottom: 2px; color: var(--ink); }
  .copy { font-size: 7px; line-height: 13px; white-space: nowrap; color: var(--ink); }
  .view-all { display: block; margin-top: 8px; font-size: 6.5px; color: var(--ink); }
  .products {
    position: absolute; left: 457px; top: 333px; width: 322px; height: 600px;
    background: var(--panel); padding: 18px 13px 0 18px;
  }
  .products .section-title { color: var(--heading-tan); margin-left: -1px; margin-bottom: 14px; }
  .product-card {
    display: flex; width: 291px; height: 128px; background: var(--white);
    padding: 12px 0 0 11px; margin-bottom: 8px;
  }
  .product-photo { width: 109px; height: 102px; flex: none; }
  .product-info { padding-left: 8px; width: 162px; position: relative; }
  .product-name { font-size: 10px; line-height: 12px; font-weight: 400; color: var(--title-red); margin-bottom: 11px; white-space: nowrap; }
  .continue { position: absolute; left: 6px; top: 93px; font-size: 6.5px; font-style: italic; color: var(--muted); }
  .social { position: absolute; left: 794px; top: 450px; color: var(--white); }
  .social-icons { display: flex; gap: 3px; margin-top: 20px; margin-left: 1px; }
  .social-icons span { width: 18px; height: 18px; background: var(--icon); display: block; }
</style>
</head>
<body>
  <div class="sand-band"></div>

  <header>
    <div class="brand">
      <span class="brand-mark"></span>
      <div class="brand-text">
        <span class="brand-name">Tidewell Botanics</span>
        <span class="brand-tagline">organic soap</span>
      </div>
    </div>
    <nav class="main-nav">
      <a class="is-active" href="#">Home</a>
      <a href="#" style="left:106px">About Us</a>
      <a href="#" style="left:186px">Soap</a>
      <a href="#" style="left:272px">Lorem Ipsum</a>
      <a href="#" style="left:358px">Contact Us</a>
    </nav>
  </header>

  <div class="hero" role="img" aria-label="Photo of stacked cream organic soap bars tied with twine, green leaves and a bowl of bath salts"></div>

  <aside class="latest">
    <h2 class="section-title">Latest Update</h2>
    <div class="update">
      <div class="update-date">16, Feb 2014</div>
      <p class="copy">Lorem ipsum dolor sit amet, consectetur adipisic-<br>ing elit, sed do eiusmod tempor incididunt ut<br>labore et dolore magna aliqua. Ut enim ad minim<br>veniam</p>
    </div>
    <div class="update">
      <div class="update-date">16, Feb 2014</div>
      <p class="copy">Lorem ipsum dolor sit amet, consectetur adipisic-<br>ing elit, sed do eiusmod tempor incididunt ut<br>labore et dolore magna aliqua. Ut enim ad minim<br>veniam</p>
    </div>
    <a class="view-all" href="#">view all &gt;&gt;</a>
  </aside>

  <main class="products">
    <h2 class="section-title">Our Products</h2>
    <article class="product-card">
      <div class="product-photo" role="img" aria-label="Photo of a lavender soap bar" style="background:#a9a4c8"></div>
      <div class="product-info">
        <h3 class="product-name">Lorem ipsum dolor sit amet</h3>
        <p class="copy">Lorem ipsum dolor sit amet, consectetur adipisic-<br>ing elit, sed do eiusmod tempor incididunt ut<br>labore et dolore magna aliqua. Ut enim ad minim<br>veniam</p>
        <a class="continue" href="#">continue &gt;&gt;</a>
      </div>
    </article>
    <article class="product-card">
      <div class="product-photo" role="img" aria-label="Photo of cream soap bars on a wooden board" style="background:#d8cf9c"></div>
      <div class="product-info">
        <h3 class="product-name">Lorem ipsum dolor sit amet</h3>
        <p class="copy">Lorem ipsum dolor sit amet, consectetur adipisic-<br>ing elit, sed do eiusmod tempor incididunt ut<br>labore et dolore magna aliqua. Ut enim ad minim<br>veniam</p>
        <a class="continue" href="#">continue &gt;&gt;</a>
      </div>
    </article>
    <article class="product-card">
      <div class="product-photo" role="img" aria-label="Photo of layered yellow and purple handmade soap bars" style="background:#d6c58e"></div>
      <div class="product-info">
        <h3 class="product-name">Lorem ipsum dolor sit amet</h3>
        <p class="copy">Lorem ipsum dolor sit amet, consectetur adipisic-<br>ing elit, sed do eiusmod tempor incididunt ut<br>labore et dolore magna aliqua. Ut enim ad minim<br>veniam</p>
        <a class="continue" href="#">continue &gt;&gt;</a>
      </div>
    </article>
    <article class="product-card">
      <div class="product-photo" role="img" aria-label="Photo of pale green herbal soap slices" style="background:#cfe0b0"></div>
      <div class="product-info">
        <h3 class="product-name">Lorem ipsum dolor sit amet</h3>
        <p class="copy">Lorem ipsum dolor sit amet, consectetur adipisic-<br>ing elit, sed do eiusmod tempor incididunt ut<br>labore et dolore magna aliqua. Ut enim ad minim<br>veniam</p>
        <a class="continue" href="#">continue &gt;&gt;</a>
      </div>
    </article>
  </main>

  <aside class="social">
    <h2 class="section-title">Social Links</h2>
    <div class="social-icons">
      <span></span><span></span><span></span>
      <span><svg width="18" height="18" viewBox="0 0 18 18"><path d="M9 4.5v9M4.5 9h9" stroke="#fff" stroke-width="2.2"/></svg></span>
    </div>
  </aside>

  <footer class="site-footer">
    Copyright 2014 All Right Reserved Company Name.
  </footer>
</body>
</html>
```